Pull up banner design for mortgage broking firm $500 competition

Need a pull up banner design the banner will be
1.8m banner tall
Colours should be similar to our Logo blues and yellows
The logo at the top
the cloud house needs to be in the middle
the $500 needs to be big and stand out
The terms and conditions should be in dot points
the top line to be bigger than the bottom and different colour font.
Please see the attached dot point design down the bottom - but use yellow and blue colours.
the licensee details need to be in small print down the bottom.
Mortgage

```html
<!DOCTYPE html>
<html lang="en">
<head>
<meta charset="utf-8">
<title>Kindred Home Loans – Pull Up Banner</title>
<link href="https://fonts.googleapis.com/css2?family=Arimo:wght@400;700&display=swap" rel="stylesheet">
<style>
  :root {
    --backdrop: #3a3739;
    --paper: #ffffff;
    --navy: #0d3768;
    --brand-blue: #0b6fc0;
    --sky-top: #2f6fbf;
    --sky-mid: #6ea3dc;
    --panel: #0f3b6f;
    --accent-yellow: #f5c400;
    --heading-yellow: #ffd21f;
    --ink-grey: #444444;
  }
  * { box-sizing: border-box; margin: 0; padding: 0; }
  html, body { width: 1200px; height: 2449px; overflow: hidden; }
  body {
    background: var(--backdrop);
    font-family: "Arimo", Arial, sans-serif;
    position: relative;
  }
  .banner {
    position: absolute;
    left: 100px; top: 98px;
    width: 1000px; height: 2253px;
    background: var(--paper);
    overflow: hidden;
  }
  .brand-header {
    height: 290px;
    display: flex; align-items: center; justify-content: center; gap: 22px;
  }
  .brand-mark {
    width: 96px; height: 96px; border-radius: 50%;
    background: var(--brand-blue);
  }
  .brand-name {
    font-weight: 700; font-size: 62px; color: var(--brand-blue);
    letter-spacing: 1px; line-height: 1;
  }
  .hero-sky {
    position: absolute; left: 0; top: 290px;
    width: 1000px; height: 1110px;
    background: linear-gradient(180deg, var(--sky-top) 0%, var(--sky-mid) 45%, #d8e7f6 80%, var(--paper) 100%);
  }
  .headline {
    position: absolute; left: 110px; top: 848px;
    font-weight: 700; font-size: 78px; line-height: 1.04; color: var(--navy);
  }
  .prize {
    position: absolute; left: 104px; top: 1012px;
    font-weight: 700; font-size: 236px; line-height: 1; color: var(--brand-blue);
    letter-spacing: 0;
    text-shadow: 0 0 24px #ffffff, 0 0 10px #ffffff;
  }
  .offer {
    position: absolute; left: 114px; top: 1239px;
    font-size: 48px; line-height: 1.15; color: var(--navy);
  }
  .offer strong { font-weight: 700; }
  .terms-title {
    position: absolute; left: 104px; top: 1408px;
    font-weight: 700; font-size: 26px; color: var(--ink-grey);
  }
  .terms-list { list-style: none; }
  .term {
    position: absolute; left: 108px; width: 788px;
    background: var(--panel);
    border-left: 12px solid var(--accent-yellow);
    display: flex; align-items: center;
    padding: 0 40px 0 0;
  }
  .term-tick { width: 104px; flex: none; display: flex; justify-content: center; }
  .term-tick svg { width: 44px; height: 40px; }
  .term-text { font-size: 22px; line-height: 1.2; color: #ffffff; }
  .term-heading { display: block; font-weight: 700; color: var(--heading-yellow); }
  .licensee {
    position: absolute; left: 108px; top: 2158px;
    font-size: 16px; line-height: 1.7; color: var(--ink-grey);
  }
</style>
</head>
<body>
  <main class="banner">
    <header class="brand-header">
      <span class="brand-mark"></span>
      <span class="brand-name">KINDRED HOME LOANS</span>
    </header>

    <div class="hero-sky" role="img" aria-label="Blue sky with a house shape formed from white clouds"></div>

    <h1 class="headline">We give you savings<br>or we give you</h1>
    <div class="prize">$500</div>
    <p class="offer">Free home loan health check with<br>a <strong>KHL</strong> lending adviser!</p>

    <h2 class="terms-title">Terms and conditions</h2>
    <ul class="terms-list">
      <li class="term" style="top:1447px;height:96px">
        <span class="term-tick"><svg viewBox="0 0 44 40"><path d="M3 22 L15 34 L41 4" fill="none" stroke="#ffd21f" stroke-width="6" stroke-linecap="round" stroke-linejoin="round"/></svg></span>
        <span class="term-text"><span class="term-heading">Our Kindred policy is where the savings start</span>All calculations of savings include KHL Kindred policy of 0.15% on the running balance of your loan.</span>
      </li>
      <li class="term" style="top:1559px;height:63px">
        <span class="term-tick"><svg viewBox="0 0 44 40"><path d="M3 22 L15 34 L41 4" fill="none" stroke="#ffd21f" stroke-width="6" stroke-linecap="round" stroke-linejoin="round"/></svg></span>
        <span class="term-text"><span class="term-heading">At least $300,000 loan</span>Your current loan size needs to be a minimum of $300,000.</span>
      </li>
      <li class="term" style="top:1634px;height:96px">
        <span class="term-tick"><svg viewBox="0 0 44 40"><path d="M3 22 L15 34 L41 4" fill="none" stroke="#ffd21f" stroke-width="6" stroke-linecap="round" stroke-linejoin="round"/></svg></span>
        <span class="term-text"><span class="term-heading">Must be local and in person.</span>Your appointment must be within 35km of Melbourne CBD and face-to-face with a KHL adviser.</span>
      </li>
      <li class="term" style="top:1744px;height:68px">
        <span class="term-tick"><svg viewBox="0 0 44 40"><path d="M3 22 L15 34 L41 4" fill="none" stroke="#ffd21f" stroke-width="6" stroke-linecap="round" stroke-linejoin="round"/></svg></span>
        <span class="term-text"><span class="term-heading">The client must currently reside there.</span>Your current loan must be for the home you currently reside in.</span>
      </li>
      <li class="term" style="top:1826px;height:96px">
        <span class="term-tick"><svg viewBox="0 0 44 40"><path d="M3 22 L15 34 L41 4" fill="none" stroke="#ffd21f" stroke-width="6" stroke-linecap="round" stroke-linejoin="round"/></svg></span>
        <span class="term-text"><span class="term-heading">Must be with Big 4 home loans only Ardent, Coastal, Northway or Westmere branded home loans</span>Must be a big four loan easily accessible by the public.</span>
      </li>
      <li class="term" style="top:1934px;height:117px">
        <span class="term-tick"><svg viewBox="0 0 44 40"><path d="M3 22 L15 34 L41 4" fill="none" stroke="#ffd21f" stroke-width="6" stroke-linecap="round" stroke-linejoin="round"/></svg></span>
        <span class="term-text"><span class="term-heading">Must be an owner occupied loan with a Variable Rate and principal interest repayments</span>All three of the above criteria must be met (KHL specifically exclude investment loans, fixed interest and interest only loans.</span>
      </li>
      <li class="term" style="top:2062px;height:70px">
        <span class="term-tick"><svg viewBox="0 0 44 40"><path d="M3 22 L15 34 L41 4" fill="none" stroke="#ffd21f" stroke-width="6" stroke-linecap="round" stroke-linejoin="round"/></svg></span>
        <span class="term-text"><span class="term-heading">The loan must be at least 30 months old.</span>Must be at least 30 months since day of settlement.</span>
      </li>
    </ul>

    <p class="licensee">Evenfield Lending Pty Ltd Trading As Kindred Home Loans ABN 40 271 903 618,<br>Authorised Representative of Southern Finance Group ABN 52 184 730 266, Australian Credit License 512 364.</p>
  </main>
</body>
</html>
```